Corporate PowerPoint design for edtech focused on developing world / emerging markets

I am involved in a edtech startup focused on providing financial literacy for students and young adults in the developing world and emerging markets; currently focus will be on Africa. We are in discussions with the CEO of a bank in S. Africa and would deploy products throughout much of Africa with them. I need a corporate powerpoint that I can use for my customers and for investor presentation. Company name is Tidecrest, which is a surfing term; meant to connotate movement and energy.
Updates

Target Market(s)

target market is two fold - will be selling to execs at banks and telecommunications companies; also need to present to investors.

Industry/Entity Type

Financial

Font styles to use
Sans Serif

Requirements
Must have
• I'd like to have a slide or two that allow me to do columns for things like feature / benefits or just content that doesn't run left to right across the entire powepoint page.
• otherwise, too much color (other than white) uses a ton of ink, so I don't want a full color background e.g. I don't want a blue or green background. I would like to provide some standard corporate info at the bottom - just basics of contact info, url and ability to change them as necessary

```html
<!DOCTYPE html>
<html lang="en">
<head>
<meta charset="utf-8">
<title>Tidecrest – Presentation Slides</title>
<link href="https://fonts.googleapis.com/css2?family=Roboto:wght@400;500;700&display=swap" rel="stylesheet">
<style>
  :root {
    --header-blue: #137a99;
    --teal: #17a2a2;
    --teal-text: #1b9a9c;
    --ink-gray: #7a7a7a;
    --ring-gray: #a8a8a8;
    --line-gray: #dcdcdc;
    --page-bg: #e6e6e6;
    --white: #ffffff;
    --check: #15607a;
  }
  html, body {
    margin: 0;
    padding: 0;
    width: 1200px;
    height: 2738px;
    overflow: hidden;
    background: var(--page-bg);
    font-family: "Roboto", Arial, sans-serif;
  }
  .board { position: relative; width: 1200px; height: 2738px; }

  .slide {
    position: absolute;
    background: var(--white);
    overflow: hidden;
    box-shadow: 0 18px 30px rgba(0,0,0,0.18);
  }
  .slide--charts { left: 52px; top: 32px; width: 1098px; height: 830px; }
  .slide--bullets { left: 55px; top: 915px; width: 1108px; height: 832px; }
  .slide--testimonials { left: 39px; top: 1827px; width: 1120px; height: 842px; }

  .slide-header {
    position: absolute; left: 0; top: 0; width: 100%; height: 125px;
    background: var(--header-blue);
  }
  .slide-header::after {
    content: ""; position: absolute; left: 96px; bottom: -14px;
    border-left: 15px solid transparent; border-right: 15px solid transparent;
    border-top: 15px solid var(--header-blue);
  }
  .slide-title {
    position: absolute; left: 66px; top: 36px; margin: 0;
    color: var(--white); font-weight: 400; font-size: 40px; letter-spacing: 5px;
  }
  .brand {
    position: absolute; right: 68px; top: 40px;
    color: var(--white); font-weight: 700; font-size: 38px; letter-spacing: 0.5px;
    display: flex; align-items: center; gap: 12px;
  }
  .brand-dot { width: 30px; height: 30px; border-radius: 50%; background: var(--white); }

  /* charts */
  .stat { position: absolute; top: 300px; width: 340px; margin-left: -170px; text-align: center; }
  .stat svg { display: block; margin: 0 auto; }
  .stat-value { margin: 14px 0 6px; color: var(--teal-text); font-size: 56px; font-weight: 400; letter-spacing: 2px; }
  .stat-caption { margin: 0; color: var(--ink-gray); font-size: 17px; line-height: 22px; }

  /* footer */
  .slide-footer { position: absolute; left: 52px; right: 52px; height: 70px; border-top: 2px solid var(--line-gray); }
  .slide--charts .slide-footer { top: 748px; }
  .slide--bullets .slide-footer { top: 757px; }
  .footer-brand {
    position: absolute; left 0; left: 0; top: 18px;
    color: var(--header-blue); font-weight: 700; font-size: 32px;
    display: flex; align-items: center; gap: 10px;
  }
  .footer-brand .brand-dot { width: 24px; height: 24px; background: var(--teal); }
  .footer-url {
    position: absolute; left: 50%; top: 28px; transform: translateX(-50%);
    color: var(--ink-gray); font-size: 17px; letter-spacing: 6px;
  }
  .footer-nav { position: absolute; right: 0; top: 22px; display: flex; gap: 10px; }

  /* bullets */
  .bullet-list { position: absolute; left: 52px; top: 250px; margin: 0; padding: 0; list-style: none; }
  .bullet-list li { position: relative; height: 99px; padding-left: 44px; color: var(--ink-gray); font-size: 17px; line-height: 23px; }
  .bullet-list svg { position: absolute; left: 0; top: 12px; }
  .photo-house {
    position: absolute; left: 474px; top: 157px; width: 570px; height: 552px;
    background: radial-gradient(ellipse at 55% 45%, #d9dcc8 0%, #b9bfa3 45%, #8f9a82 75%, #ffffff 100%);
  }

  /* testimonials */
  .quote-band {
    position: absolute; left: 0; top: 292px; width: 100%; height: 360px;
    background: var(--teal); color: var(--white); text-align: center;
  }
  .quote-text { margin: 86px auto 0; width: 940px; font-size: 19px; line-height: 36px; }
  .quote-mark { position: absolute; font-size: 60px; line-height: 1; color: var(--header-blue); font-weight: 700; }
  .quote-mark--open { left: 345px; top: 50px; }
  .quote-mark--close { left: 686px; top: 176px; }
  .portrait {
    position: absolute; left: 473px; top: 561px; width: 174px; height: 174px; border-radius: 50%;
    background: linear-gradient(160deg, #5a6f80 0%, #3b4550 60%, #262c33 100%);
    box-shadow: 0 0 0 4px var(--teal);
  }
</style>
</head>
<body>
<div class="board">

  <section class="slide slide--charts">
    <header class="slide-header">
      <h1 class="slide-title">GRAPHIC CHARTS</h1>
      <div class="brand">Tidecrest<span class="brand-dot"></span></div>
    </header>

    <div class="stat" style="left:164px">
      <svg width="130" height="130" viewBox="0 0 130 130">
        <circle cx="65" cy="65" r="54" fill="none" stroke="var(--ring-gray)" stroke-width="18"/>
        <circle cx="65" cy="65" r="54" fill="none" stroke="var(--header-blue)" stroke-width="18"
                stroke-dasharray="254.5 339.3" transform="rotate(-90 65 65)"/>
        <rect x="44" y="60" width="32" height="24" rx="3" fill="var(--ring-gray)"/>
        <path d="M76 66 L88 58 V86 L76 78 Z" fill="var(--ring-gray)"/>
        <circle cx="52" cy="52" r="8" fill="var(--ring-gray)"/>
        <circle cx="68" cy="52" r="8" fill="var(--ring-gray)"/>
      </svg>
      <p class="stat-value">75%</p>
      <p class="stat-caption">industry. Lorem Ipsum has<br>been the industry's standard</p>
    </div>

    <div class="stat" style="left:525px">
      <svg width="130" height="130" viewBox="0 0 130 130">
        <circle cx="65" cy="65" r="54" fill="none" stroke="var(--ring-gray)" stroke-width="18"/>
        <circle cx="65" cy="65" r="54" fill="none" stroke="var(--header-blue)" stroke-width="18"
                stroke-dasharray="84.8 339.3" transform="rotate(-90 65 65)"/>
        <path d="M45 50 H85 V76 H62 L52 85 V76 H45 Z" fill="var(--ring-gray)"/>
      </svg>
      <p class="stat-value">25%</p>
      <p class="stat-caption">industry. Lorem Ipsum has<br>been the industry's standard</p>
    </div>

    <div class="stat" style="left:912px">
      <svg width="130" height="130" viewBox="0 0 130 130">
        <circle cx="65" cy="65" r="54" fill="none" stroke="var(--ring-gray)" stroke-width="18"/>
        <circle cx="65" cy="65" r="54" fill="none" stroke="var(--header-blue)" stroke-width="18"
                stroke-dasharray="169.6 339.3" transform="rotate(-90 65 65)"/>
        <rect x="44" y="54" width="42" height="30" rx="3" fill="var(--ring-gray)"/>
        <path d="M57 54 V48 H73 V54" fill="none" stroke="var(--ring-gray)" stroke-width="4"/>
      </svg>
      <p class="stat-value">50%</p>
      <p class="stat-caption">industry. Lorem Ipsum has<br>been the industry's standard</p>
    </div>

    <footer class="slide-footer">
      <div class="footer-brand">Tidecrest<span class="brand-dot"></span></div>
      <div class="footer-url">www.tidecrest.org</div>
      <nav class="footer-nav" aria-label="Slide navigation">
        <svg width="30" height="30" viewBox="0 0 30 30"><circle cx="15" cy="15" r="13" fill="none" stroke="var(--teal)" stroke-width="2"/><path d="M17 9 L11 15 L17 21" fill="none" stroke="var(--teal)" stroke-width="2.5"/></svg>
        <svg width="30" height="30" viewBox="0 0 30 30"><circle cx="15" cy="15" r="13" fill="none" stroke="var(--teal)" stroke-width="2"/><path d="M15 8 V22 M8 15 H22" stroke="var(--teal)" stroke-width="2.5"/></svg>
        <svg width="30" height="30" viewBox="0 0 30 30"><circle cx="15" cy="15" r="13" fill="none" stroke="var(--teal)" stroke-width="2"/><path d="M13 9 L19 15 L13 21" fill="none" stroke="var(--teal)" stroke-width="2.5"/></svg>
      </nav>
    </footer>
  </section>

  <section class="slide slide--bullets">
    <header class="slide-header">
      <h1 class="slide-title">BULLET IN TEXTS</h1>
      <div class="brand">Tidecrest<span class="brand-dot"></span></div>
    </header>

    <ul class="bullet-list">
      <li><svg width="28" height="24" viewBox="0 0 28 24"><path d="M3 13 L10 20 L25 4" fill="none" stroke="var(--check)" stroke-width="4.5"/></svg>industry. Lorem Ipsum has<br>been the industry's standard</li>
      <li><svg width="28" height="24" viewBox="0 0 28 24"><path d="M3 13 L10 20 L25 4" fill="none" stroke="var(--check)" stroke-width="4.5"/></svg>industry. Lorem Ipsum has<br>been the industry's standard</li>
      <li><svg width="28" height="24" viewBox="0 0 28 24"><path d="M3 13 L10 20 L25 4" fill="none" stroke="var(--check)" stroke-width="4.5"/></svg>industry. Lorem Ipsum has<br>been the industry's standard</li>
      <li><svg width="28" height="24" viewBox="0 0 28 24"><path d="M3 13 L10 20 L25 4" fill="none" stroke="var(--check)" stroke-width="4.5"/></svg>industry. Lorem Ipsum has<br>been the industry's standard</li>
      <li><svg width="28" height="24" viewBox="0 0 28 24"><path d="M3 13 L10 20 L25 4" fill="none" stroke="var(--check)" stroke-width="4.5"/></svg>industry. Lorem Ipsum has<br>been the industry's standard</li>
    </ul>

    <div class="photo-house" role="img" aria-label="Photo of a small house folded from banknotes"></div>

    <footer class="slide-footer">
      <div class="footer-brand">Tidecrest<span class="brand-dot"></span></div>
      <div class="footer-url">www.tidecrest.org</div>
      <nav class="footer-nav" aria-label="Slide navigation">
        <svg width="30" height="30" viewBox="0 0 30 30"><circle cx="15" cy="15" r="13" fill="none" stroke="var(--teal)" stroke-width="2"/><path d="M17 9 L11 15 L17 21" fill="none" stroke="var(--teal)" stroke-width="2.5"/></svg>
        <svg width="30" height="30" viewBox="0 0 30 30"><circle cx="15" cy="15" r="13" fill="none" stroke="var(--teal)" stroke-width="2"/><path d="M15 8 V22 M8 15 H22" stroke="var(--teal)" stroke-width="2.5"/></svg>
        <svg width="30" height="30" viewBox="0 0 30 30"><circle cx="15" cy="15" r="13" fill="none" stroke="var(--teal)" stroke-width="2"/><path d="M13 9 L19 15 L13 21" fill="none" stroke="var(--teal)" stroke-width="2.5"/></svg>
      </nav>
    </footer>
  </section>

  <section class="slide slide--testimonials">
    <header class="slide-header">
      <h1 class="slide-title">TESTIMONIALS</h1>
      <div class="brand">Tidecrest<span class="brand-dot"></span></div>
    </header>

    <div class="quote-band">
      <span class="quote-mark quote-mark--open">&ldquo;</span>
      <p class="quote-text">industry. Lorem Ipsum has<br>industry. Lorem Ipsum has industry. Lorem Ipsum has industry. Lorem Ipsum has industry. Lorem Ipsum has<br>industry. Lorem Ipsum has industry. Lorem Ipsum has industry. Lorem Ipsum has<br>industry. Lorem Ipsum has</p>
      <span class="quote-mark quote-mark--close">&rdquo;</span>
    </div>

    <div class="portrait" role="img" aria-label="Round portrait photo of the person giving the testimonial"></div>
  </section>

</div>
</body>
</html>
```